I want to revise my business card design and get a more modern and up to date design.

Brolvane Handyman Sevices originated from a family-owned and operated contractor business, performing home renovation, addition, and construction work in the NYC area since 2004. Today, we specialize in reliable and affordable handyman services for residential and commercial clients In 2014, we expanded to northern New Jersey. In 2016, we brought quality home improvement and repair services to new Bucks County, PA, and nearby New Jersey areas.
Target Market(s)
Home owners and business that might be looking for a General contractor, handyman, cleaning services and Home maintenance and property.
Industry/Entity Type
Construction Company
Contact Information for Business Card
I am open to new ideas
Colors
Designer to choose colors to be used in the design.
Look and feel
Each slider illustrates characteristics of the customer's brand and the style your logo design should communicate.

```html
<!DOCTYPE html>
<html lang="en">
<head>
<meta charset="utf-8">
<title>Brolvane Handyman Sevices – Business Card</title>
<link rel="stylesheet" href="https://fonts.googleapis.com/css2?family=Montserrat:wght@400;600;800&family=Arimo:wght@400&display=swap">
<style>
  :root {
    --scene: #141414;
    --card: #262626;
    --red: #e31b23;
    --white: #ffffff;
    --grey: #d9d9d9;
    --teal: #6fb8b0;
    --orange: #f07c22;
  }
  * { margin: 0; padding: 0; box-sizing: border-box; }
  html, body { width: 1200px; height: 912px; overflow: hidden; }
  body {
    background: var(--scene);
    font-family: "Montserrat", sans-serif;
    color: var(--white);
    position: relative;
  }
  .card {
    position: absolute;
    width: 560px;
    height: 320px;
    background: var(--card);
    box-shadow: 0 20px 40px rgba(0,0,0,.6);
    overflow: hidden;
  }
  .card--front { left: 50px; top: 110px; }
  .card--back { left: 590px; top: 482px; }

  .brand { display: flex; align-items: center; gap: 14px; }
  .brand__dot { width: 26px; height: 26px; border-radius: 50%; background: var(--red); flex: none; }
  .brand__text { display: flex; flex-direction: column; }
  .brand__name { font-weight: 800; line-height: 1; color: var(--white); white-space: nowrap; }
  .brand__tag { font-weight: 400; letter-spacing: .34em; color: var(--white); margin-top: 6px; white-space: nowrap; }

  .card--front .brand { position: absolute; left: 120px; top: 70px; }
  .card--front .brand__name { font-size: 56px; }
  .card--front .brand__tag { font-size: 11px; }

  .partner { position: absolute; font-weight: 600; font-size: 20px; white-space: nowrap; }
  .partner--home { left: 200px; top: 215px; color: var(--teal); }
  .partner--local { left: 390px; top: 168px; color: var(--orange); display: flex; align-items: center; gap: 8px; }
  .partner--local .partner__mark { width: 14px; height: 14px; background: var(--orange); }
  .badge {
    position: absolute; left: 40px; top: 255px;
    width: 120px; height: 44px; background: var(--red);
  }
  .badge__inner { position: absolute; left: 6px; top: 8px; width: 108px; height: 12px; background: var(--white); }

  .card--back .brand { position: absolute; left: 36px; top: 110px; gap: 12px; }
  .card--back .brand__dot { width: 20px; height: 20px; }
  .card--back .brand__name { font-size: 38px; }
  .card--back .brand__tag { font-size: 8px; }

  .divider { position: absolute; left: 272px; top: 40px; width: 2px; height: 130px; background: var(--red); }
  .contact { position: absolute; left: 290px; top: 52px; }
  .contact__name { color: var(--red); font-weight: 600; font-size: 22px; margin-bottom: 10px; white-space: nowrap; }
  .contact__row { display: flex; align-items: center; gap: 8px; font-size: 12px; color: var(--grey); margin-bottom: 6px; white-space: nowrap; }
  .contact__row svg { width: 12px; height: 12px; flex: none; }

  .services {
    position: absolute; left: 0; right: 0; top: 218px;
    font-family: "Arimo", sans-serif; text-transform: uppercase; text-align: center;
    color: var(--white); white-space: nowrap;
  }
  .services__line { font-size: 14px; margin-bottom: 6px; }
  .services__sep { color: var(--red); margin: 0 5px; }
  .band { position: absolute; left: 0; right: 0; bottom: 0; height: 12px; background: var(--red); }
</style>
</head>
<body>

<section class="card card--front">
  <div class="brand">
    <span class="brand__dot"></span>
    <div class="brand__text">
      <span class="brand__name">Brolvane</span>
      <span class="brand__tag">HANDYMAN SERVICES</span>
    </div>
  </div>
  <div class="partner partner--local"><span class="partner__mark"></span>Nearby Pro</div>
  <div class="partner partner--home">Kestrel Home Pros</div>
  <div class="badge" role="img" aria-label="Review listing badge"><span class="badge__inner"></span></div>
</section>

<section class="card card--back">
  <div class="brand">
    <span class="brand__dot"></span>
    <div class="brand__text">
      <span class="brand__name">Brolvane</span>
      <span class="brand__tag">HANDYMAN SERVICES</span>
    </div>
  </div>
  <div class="divider"></div>
  <div class="contact">
    <p class="contact__name">Marco Teixeira</p>
    <p class="contact__row">
      <svg viewBox="0 0 24 24" aria-hidden="true"><path fill="#e31b23" d="M6.6 10.8a15.1 15.1 0 0 0 6.6 6.6l2.2-2.2c.3-.3.7-.4 1-.2 1.1.4 2.3.6 3.6.6.6 0 1 .4 1 1V20c0 .6-.4 1-1 1A17 17 0 0 1 3 4c0-.6.4-1 1-1h3.5c.6 0 1 .4 1 1 0 1.3.2 2.5.6 3.6.1.3 0 .7-.2 1z"/></svg>
      (215) 555-0142
    </p>
    <p class="contact__row">
      <svg viewBox="0 0 24 24" aria-hidden="true"><path fill="#e31b23" d="M2 5h20v14H2z"/><path fill="none" stroke="#262626" stroke-width="2" d="M2 5l10 8 10-8"/></svg>
      brolvanehandyman@mailbox.com
    </p>
  </div>
  <div class="services">
    <p class="services__line">Repair<span class="services__sep">•</span>Improve<span class="services__sep">•</span>Remodel</p>
    <p class="services__line">Comercial and Residential Contractor<span class="services__sep">•</span>Handyman<span class="services__sep">•</span>Technician</p>
  </div>
  <div class="band"></div>
</section>

</body>
</html>
```